Copper Lantern LLC Business Card

We need a business card design for a newco in Texas. We are a team of professionals who join start ups as founders and help launch their businesses, which are primarily related to food and beverage and the service side of the industry. We love local and craft and are partners in businesses in the local meat, BBQ and Burger, fine dining, and beverage alcohol businesses. Our specialty is finance and the business side of start ups, including assisting with capital raises as principals, not brokers. We do not currently have any logos or graphics for this entity. Our values include helping people succeed, rooting for the underdog, healthy food, the environment and being good citizens.

Target Market(s)

Everybody but also Angel Investors, CPAs, Bankers, Entrepreneurs

Industry/Entity Type

Business

Contact Information for Business Card

Fields for Business Name, Title, Email Address, Phone Number. Place to add mailing address and web domain later.

Font styles to use
Sans Serif

Colors

Designer to choose colors to be used in the design.

Requirements
Should not have
• Pictures of booze bottles or drinks thought there could be a social scene that does not strictly focus on those. No cows, cowboy hats or ranches. We are not a Wall Street type entity so no huge office buildings or skylines.

```html
<!DOCTYPE html>
<html lang="en">
<head>
<meta charset="utf-8">
<title>Copper Lantern LLC Business Card</title>
<link href="https://fonts.googleapis.com/css2?family=Exo+2:wght@600;700;800&display=swap" rel="stylesheet">
<style>
  :root {
    --page: #e9e4dc;
    --orange-light: #f79a2a;
    --orange: #ee7a16;
    --orange-deep: #d9560e;
    --black: #0d0b09;
    --gold: #e8b22b;
    --white: #ffffff;
    --ink: #1a1208;
  }
  * { margin: 0; padding: 0; box-sizing: border-box; }
  html, body { width: 1200px; height: 780px; overflow: hidden; }
  body {
    background: var(--page);
    font-family: "Exo 2", sans-serif;
    display: flex; align-items: center; justify-content: center;
  }
  .card {
    position: relative;
    width: 1050px; height: 600px;
    background: var(--black);
    overflow: hidden;
    box-shadow: 0 14px 34px rgba(0,0,0,.25);
  }
  .card__header {
    position: absolute; left: 0; top: 0; width: 100%; height: 300px;
    background: radial-gradient(ellipse at 30% 30%, var(--orange-light), var(--orange) 55%, var(--orange-deep));
  }
  .company-name {
    position: absolute; left: 52px; bottom: 34px;
    font-size: 78px; font-weight: 800; color: var(--white);
    letter-spacing: 1px;
    text-shadow: 3px 3px 0 var(--ink), -1px -1px 0 var(--ink), 2px -1px 0 var(--ink), -1px 2px 0 var(--ink);
  }
  .contact-person {
    position: absolute; right: 50px; top: 34px; text-align: left;
    color: var(--white);
    text-shadow: 2px 2px 0 var(--ink), -1px -1px 0 var(--ink);
  }
  .contact-person__name { font-size: 40px; font-weight: 700; }
  .contact-person__phone {
    display: flex; align-items: center; gap: 10px;
    font-size: 36px; font-weight: 700; margin-top: 4px;
  }
  .phone-icon { width: 30px; height: 30px; flex: none; }
  .divider {
    position: absolute; left: 0; width: 100%; height: 22px;
    background: var(--black);
    border-top: 4px solid var(--gold);
  }
  .divider--top { top: 300px; }
  .photo-strip {
    position: absolute; left: 0; top: 322px; width: 100%; height: 170px;
    display: grid; grid-template-columns: repeat(4, 1fr); gap: 8px;
    background: var(--black); padding: 0 0 0 0;
  }
  .photo { height: 100%; }
  .photo--grill { background: linear-gradient(135deg, #8a2a12, #e0581c 50%, #f2a65a); }
  .photo--burger { background: linear-gradient(135deg, #e8c488, #b0421f 55%, #6e7a2a); }
  .photo--skewers { background: linear-gradient(135deg, #3a2a22, #f0a030 50%, #7a3a1c); }
  .photo--wrap { background: linear-gradient(135deg, #f2d27a, #c98a6a 55%, #8c3a3a); }
  .card__footer {
    position: absolute; left: 0; top: 492px; width: 100%; height: 108px;
    background: var(--black);
    border-top: 4px solid var(--gold);
    box-shadow: inset 0 10px 0 var(--black), inset 0 14px 0 var(--gold);
    display: flex; align-items: center; padding: 14px 52px 0;
    font-size: 30px; font-weight: 600; color: var(--gold);
  }
  .footer__label { font-weight: 800; margin-right: 10px; }
  .footer__sep { margin: 0 18px; }
</style>
</head>
<body>
  <div class="card">
    <header class="card__header">
      <div class="contact-person">
        <div class="contact-person__name">Dana Whitfield</div>
        <div class="contact-person__phone">
          <svg class="phone-icon" viewBox="0 0 24 24" aria-hidden="true">
            <rect width="24" height="24" rx="4" fill="#1a1208"/>
            <path d="M7 5c1 0 2 2.5 2 3.2 0 .8-1.2 1.2-1 2 .6 2 2.4 3.8 4.6 4.6.8.2 1.2-1 2-1 .7 0 3.2 1 3.2 2 0 1.2-1.4 2.4-2.6 2.4C10 18.2 5.8 14 5.6 8 5.6 6.4 6 5 7 5z" fill="#fff"/>
          </svg>
          0145 872 360
        </div>
      </div>
      <h1 class="company-name">Copper Lantern LLC</h1>
    </header>
    <div class="divider divider--top"></div>
    <section class="photo-strip">
      <div class="photo photo--grill" role="img" aria-label="Sausages and meats on a flaming grill"></div>
      <div class="photo photo--burger" role="img" aria-label="Cheeseburger with lettuce and tomato"></div>
      <div class="photo photo--skewers" role="img" aria-label="Skewers cooking over open flame"></div>
      <div class="photo photo--wrap" role="img" aria-label="Toasted sandwich wrap with sliced meat"></div>
    </section>
    <footer class="card__footer">
      <span class="footer__label">E:</span> hello@copperlantern.com
      <span class="footer__sep">|</span>
      <span class="footer__label">W:</span> www.copperlantern.com
    </footer>
  </div>
</body>
</html>
```